Card for Real Estate Developer

We need a business card design for a Real Estate Development company based in Texas. We focus on retail, apartment and residential development. Our target is predominantly investors looking to us to place their money properly to achieve a significant return. On the other side we sell our services to large retailers as their preferred developer assisting them in locating, building and leasing their real estate.

Target Market(s)

Investors

Industry/Entity Type

Real Estate Development

Contact Information for Business Card

Would like to stay within the company color scheme, while keeping the design moderately simple.

Font styles to use
Other font styles liked:
• per attached document

Requirements
Must have
• Name
• Phone
• Email
• Website
• Logo Prominently Displayed
• Stay within the colors provided in the attached document

```html
<!DOCTYPE html>
<html lang="en">
<head>
<meta charset="utf-8">
<title>Harlow Ridge Development – Business Card</title>
<link href="https://fonts.googleapis.com/css2?family=Open+Sans:wght@400;600&display=swap" rel="stylesheet">
<style>
  :root {
    --page-bg: #e9ecef;
    --brand-blue: #56a2c6;
    --brand-blue-deep: #4690b5;
    --brand-blue-light: #6fb3d3;
    --ink: #3a3d42;
    --ink-soft: #55595f;
    --card-white: #ffffff;
    --band-dark: #3e4247;
  }
  * { margin: 0; padding: 0; box-sizing: border-box; }
  html, body { width: 1200px; height: 900px; overflow: hidden; }
  body { background: var(--page-bg); position: relative; font-family: "Open Sans", Arial, sans-serif; }

  .card {
    position: absolute;
    width: 700px;
    height: 400px;
    border-radius: 4px;
    overflow: hidden;
    box-shadow: 0 10px 28px rgba(0,0,0,0.22);
  }

  /* Back side */
  .card-back {
    left: 70px; top: 50px;
    background: linear-gradient(160deg, var(--brand-blue-light) 0%, var(--brand-blue) 55%, var(--brand-blue-deep) 100%);
  }
  .back-name {
    position: absolute;
    right: 48px; top: 160px;
    text-align: right;
    color: var(--card-white);
    font-size: 26px;
    font-weight: 600;
    line-height: 1.25;
  }

  /* Front side */
  .card-front {
    left: 430px; top: 450px;
    background: var(--card-white);
  }
  .contact-tab {
    position: absolute;
    left: 0; top: 48px;
    width: 40px; height: 196px;
    background: var(--brand-blue);
    border-radius: 0 6px 6px 0;
    display: flex;
    flex-direction: column;
    align-items: center;
    padding-top: 10px;
    gap: 14px;
  }
  .contact-tab svg { width: 18px; height: 18px; fill: none; stroke: var(--card-white); stroke-width: 1.8; }
  .contact-tab .icon-person { margin-bottom: 22px; }

  .contact-block { position: absolute; left: 66px; top: 50px; color: var(--ink); }
  .person-name { font-size: 20px; font-weight: 600; color: var(--brand-blue); line-height: 1.1; }
  .person-role { font-size: 14px; color: var(--ink-soft); margin-bottom: 18px; }
  .contact-line { font-size: 17px; line-height: 30px; }
  .address { margin-top: 10px; font-size: 17px; line-height: 24px; }

  .company-lockup {
    position: absolute;
    right: 48px; top: 150px;
    display: flex;
    align-items: center;
    gap: 14px;
  }
  .company-square { width: 46px; height: 46px; background: var(--brand-blue); flex: none; }
  .company-name {
    color: var(--ink);
    font-size: 24px;
    font-weight: 600;
    line-height: 1.25;
  }

  .bottom-band { position: absolute; left: 0; bottom: 0; width: 100%; height: 34px; }
</style>
</head>
<body>

  <section class="card card-back" aria-label="Card back">
    <div class="back-name">Harlow Ridge<br>Development</div>
  </section>

  <section class="card card-front" aria-label="Card front">
    <div class="contact-tab">
      <svg class="icon-person" viewBox="0 0 24 24"><circle cx="9" cy="8" r="3.5"/><path d="M2.5 20c0-4 3-6 6.5-6s6.5 2 6.5 6"/><circle cx="17" cy="9" r="2.5"/><path d="M16 14c3 0 5.5 1.6 5.5 5"/></svg>
      <svg viewBox="0 0 24 24"><path d="M6 3l3 4-2 2c1 3 4 6 7 7l2-2 4 3-2 3C10 20 4 14 3 5z"/></svg>
      <svg viewBox="0 0 24 24"><circle cx="12" cy="12" r="9"/><path d="M3 12h18M12 3c3 3 3 15 0 18M12 3c-3 3-3 15 0 18"/></svg>
      <svg viewBox="0 0 24 24"><circle cx="12" cy="12" r="4"/><path d="M16 8v6c0 2 3 2 4 0 2-6-2-11-8-11a9 9 0 100 18c2 0 3-.5 4-1"/></svg>
      <svg viewBox="0 0 24 24"><path d="M12 22s-6-7-6-12a6 6 0 0112 0c0 5-6 12-6 12z"/><circle cx="12" cy="10" r="2"/></svg>
    </div>

    <div class="contact-block">
      <div class="person-name">Dana Whitfield</div>
      <div class="person-role">Manager</div>
      <div class="contact-line">512 480 2261</div>
      <div class="contact-line">www.danawhitfield.com</div>
      <div class="contact-line">dana@harlowridge.com</div>
      <div class="address">482 Corwin Avenue<br>Suite 600, Austin Texas 78701</div>
    </div>

    <div class="company-lockup">
      <div class="company-square"></div>
      <div class="company-name">Harlow Ridge<br>Development</div>
    </div>

    <svg class="bottom-band" viewBox="0 0 700 34" preserveAspectRatio="none">
      <rect x="0" y="22" width="700" height="12" fill="var(--band-dark)"/>
      <path d="M470 34 C500 34 500 10 540 10 L700 10 L700 34 Z" fill="var(--brand-blue)"/>
    </svg>
  </section>

</body>
</html>
```